Awesome ecommerce store banner needed!

We need a sharp, clear, strong banner for one of our subcategory pages on http://www.brixmolt.com
We'd like to incorporate the following image. We'd like the background to be gray or black. We are replacing the Wireless Intercoms banner that is orange (we hate it).
WE do like our other banners, however, so please use them as reference:
SIze: 980 x 380
Two raw images of the intercom we'd like you to encorporate have been included. Choose one or the other depending on what you think would be best. If using the single angle, please duplicate it. We want two intercoms in the banner
Simple and Clean is key:
Text: Wireless Intercoms
Text Color: Can be white/off gray
Text Style: Please keep it clean in line with the website
Background: Black/gray/white

```html
<!DOCTYPE html>
<html lang="en">
<head>
<meta charset="utf-8">
<title>Wireless Intercoms – Category Banner</title>
<link href="https://fonts.googleapis.com/css2?family=Arimo:wght@400;700&display=swap" rel="stylesheet">
<style>
  :root{
    --ink-dark:#1c1c1c;
    --banner-dark:#2a2a2a;
    --white:#ffffff;
    --heading-gray:#3d3d3d;
    --accent:#e0701c;
    --sale:#c9372c;
    --nav:#2b2b2b;
    --rule:#d6d6d6;
    --text:#333333;
    --muted:#8a8a8a;
    --unit-silver:#b9b9b9;
    --unit-black:#1e1e1e;
  }
  *{box-sizing:border-box;margin:0;padding:0}
  html,body{width:1200px;height:1000px;overflow:hidden;background:var(--white)}
  body{position:relative;font-family:"Arimo",Arial,sans-serif;color:var(--text)}

  .banner{position:absolute;overflow:hidden}
  .banner-title{position:absolute;left:0;top:0;width:100%;height:100%;font-weight:700;letter-spacing:-0.03em}
  .banner-title span{position:absolute;white-space:nowrap;line-height:1;transform-origin:left top}

  /* intercom unit placeholder: silver top, black base */
  .intercom-unit{position:absolute;border-radius:12% 8% 10% 10% / 30% 25% 18% 18%;
    background:linear-gradient(180deg,var(--unit-silver) 0%,#d6d6d6 45%,#9c9c9c 70%,var(--unit-black) 71%,var(--unit-black) 100%);
    box-shadow:0 6px 14px rgba(0,0,0,.45)}

  /* Hero banner */
  .hero{left:0;top:0;width:1200px;height:465px;
    background:radial-gradient(ellipse 460px 330px at 640px 130px,#e4e4e4 0%,#9a9a9a 40%,#5e5e5e 75%,#3a3a3a 100%)}
  .hero .backdrop-device{position:absolute;left:0;top:150px;width:520px;height:315px;
    background:linear-gradient(160deg,rgba(25,25,25,.7),rgba(60,60,60,.35))}
  .hero .unit-front{left:525px;top:215px;width:380px;height:175px}
  .hero .unit-back{left:805px;top:290px;width:385px;height:175px}
  .hero .banner-title{color:var(--white);text-shadow:2px 2px 4px rgba(0,0,0,.55)}
  .hero .line-1{left:20px;top:79px;font-size:119px;transform:scaleX(1.06)}
  .hero .line-2{left:20px;top:213px;font-size:144px;transform:scaleX(.76)}

  /* Store page */
  .store{position:absolute;left:0;top:527px;width:672px;height:473px;overflow:hidden;background:var(--white)}
  .store-nav{height:28px;background:var(--nav);display:flex;align-items:center;color:var(--white);font-size:13px}
  .store-nav .nav-item{padding:0 14px;height:100%;display:flex;align-items:center;border-right:1px solid #555}
  .store-nav .nav-item svg{margin-left:4px}
  .store-search{margin-left:auto;display:flex;height:20px;margin-right:2px}
  .store-search input{width:178px;border:0;font:10px "Arimo",sans-serif;padding-left:6px;color:var(--muted);background:var(--white)}
  .store-search .search-btn{background:#e6e6e6;color:#333;font-size:11px;font-weight:700;padding:3px 5px}

  .sidebar{position:absolute;left:0;top:38px;width:152px;height:440px;background:#f4f4f4;border-right:1px solid var(--rule)}
  .sidebar h3{color:var(--accent);font-size:14px;font-weight:700;padding:18px 0 0 13px}
  .sidebar ul{list-style:none;margin:16px 0 0 12px;font-size:9px;font-weight:700;line-height:1.25}
  .sidebar li{padding-left:7px;margin-bottom:8px;position:relative}
  .sidebar li::before{content:"";position:absolute;left:0;top:4px;width:3px;height:3px;background:var(--accent);border-radius:50%}
  .shop-link{text-align:center;font-weight:700;line-height:1}
  .shop-link .or{color:var(--accent);font-size:13px}
  .shop-link .name{font-size:13px;color:var(--ink-dark)}
  .shop-link .name b{color:var(--accent)}
  .shop-home{margin-top:28px}
  .shop-gadgets{margin-top:38px}
  .shop-gadgets .name{font-size:15px}
  .testimonials{position:absolute;top:332px;left:0;width:151px;padding:0 10px;border-top:1px solid var(--rule)}
  .testimonials h4{font-size:11px;margin:26px 0 8px 1px}
  .testimonials p{font-size:8px;line-height:1.3}

  .crumbs{position:absolute;left:165px;top:50px;font-size:8.5px;color:#555}
  .crumbs b{color:var(--accent);font-weight:700}
  .page-title{position:absolute;left:165px;top:69px;width:503px;font-size:10.5px;font-weight:700;padding-bottom:6px;border-bottom:1px solid var(--rule)}

  .store .page-banner{left:167px;top:103px;width:498px;height:217px;
    background:radial-gradient(ellipse 200px 150px at 270px 55px,#e2e2e2 0%,#9a9a9a 40%,#5e5e5e 75%,#2e2e2e 100%)}
  .page-banner .backdrop-device{position:absolute;left:0;top:70px;width:218px;height:147px;background:linear-gradient(160deg,rgba(25,25,25,.7),rgba(60,60,60,.35))}
  .page-banner .unit-front{left:218px;top:110px;width:170px;height:72px}
  .page-banner .unit-back{left:333px;top:128px;width:165px;height:80px}
  .page-banner .banner-title{color:var(--white);text-shadow:1px 1px 2px rgba(0,0,0,.55)}
  .page-banner .line-1{left:7px;top:34px;font-size:60px;transform:scaleX(.89)}
  .page-banner .line-2{left:7px;top:101px;font-size:66px;transform:scaleX(.70)}

  .products{position:absolute;left:166px;top:331px;display:flex;gap:5px}
  .product{position:relative;width:122px;height:150px;border:1px solid var(--rule);padding:12px 6px 0}
  .product .thumb{display:block;width:76px;height:70px;margin:0 auto;background:linear-gradient(135deg,#d8d8d8,#8a8a8a);border-radius:2px}
  .product h5{font-size:8px;font-weight:700;margin-top:26px;line-height:1.25;color:var(--ink-dark)}
  .product .price{font-size:8px;color:var(--muted);margin-top:4px}
  .tag{position:absolute;left:0;top:-4px;background:var(--accent);color:var(--white);font-size:9.5px;padding:2px 7px 2px 6px;display:flex;align-items:center;gap:4px}
  .tag i{width:8px;height:8px;background:var(--white);border-radius:50%;display:inline-block}
  .tag.sale{background:var(--sale)}

  /* Variant banners */
  .variant-light{left:686px;top:527px;width:514px;height:200px;
    background:radial-gradient(ellipse 280px 160px at 320px 40px,#ffffff 0%,#ececec 45%,#bdbdbd 100%)}
  .variant-dark{left:686px;top:764px;width:514px;height:200px;
    background:radial-gradient(ellipse 280px 180px at 320px 30px,#f0f0f0 0%,#9c9c9c 40%,#161616 100%)}
  .variant-light .banner-title{color:var(--heading-gray);text-shadow:2px 2px 3px rgba(0,0,0,.35)}
  .variant-dark .banner-title{color:var(--white);text-shadow:1px 1px 3px rgba(0,0,0,.5)}
  .variant-light .line-1,.variant-dark .line-1{left:7px;top:30px;font-size:59px;transform:scaleX(.93)}
  .variant-light .line-2,.variant-dark .line-2{left:8px;top:90px;font-size:63px;transform:scaleX(.75)}
  .variant-light .unit-front,.variant-dark .unit-front{left:232px;top:88px;width:170px;height:88px}
  .variant-light .unit-back,.variant-dark .unit-back{left:344px;top:118px;width:170px;height:82px}
</style>
</head>
<body>

  <section class="banner hero">
    <div class="backdrop-device" role="img" aria-label="Faded close-up of an intercom control panel"></div>
    <div class="intercom-unit unit-front" role="img" aria-label="Silver and black wireless intercom unit with antenna"></div>
    <div class="intercom-unit unit-back" role="img" aria-label="Second silver and black wireless intercom unit with antenna"></div>
    <h1 class="banner-title"><span class="line-1">Wireless</span><span class="line-2">Intercoms</span></h1>
  </section>

  <section class="store">
    <nav class="store-nav">
      <div class="nav-item">Shop Home Automation<svg width="10" height="7" viewBox="0 0 10 7"><path d="M1 1l4 4 4-4" stroke="#fff" stroke-width="2" fill="none"/></svg></div>
      <div class="nav-item">Shop Cool Gadgets<svg width="10" height="7" viewBox="0 0 10 7"><path d="M1 1l4 4 4-4" stroke="#fff" stroke-width="2" fill="none"/></svg></div>
      <div class="nav-item">Top Sellers</div>
      <div class="store-search"><input type="text" value="Enter Keyword or Item#" aria-label="Search"><span class="search-btn">SEARCH</span></div>
    </nav>

    <aside class="sidebar">
      <h3>Home Automation</h3>
      <ul>
        <li>Wireless Driveway Alarm Systems &amp; Outdoor Motion Detectors</li>
        <li>Wireless Doorbell Systems</li>
        <li>Indoor Motion Sensors</li>
        <li>Remote Light Switches &amp; Wireless Power Outlet Triggers</li>
      </ul>
      <div class="shop-link shop-home"><div class="or">or SHOP</div><div class="name">Home Automation<b>›</b></div></div>
      <div class="shop-link shop-gadgets"><div class="or">or SHOP</div><div class="name">Cool Gadgets<b>›</b></div></div>
      <div class="testimonials">
        <h4>Customer Testimonials</h4>
        <p>"I found this experience very easy. There were no delays. The package arrived in a short time with no damage. I felt like I was their only customer. Brixmolt made me feel as if I was a major purchaser. They are great."</p>
      </div>
    </aside>

    <div class="crumbs">Home &gt; View All Categories... &gt; <b>Wireless Intercom Systems</b></div>
    <div class="page-title">Wireless Intercom Systems</div>

    <div class="banner page-banner">
      <div class="backdrop-device" role="img" aria-label="Faded close-up of an intercom control panel"></div>
      <div class="intercom-unit unit-front" role="img" aria-label="Wireless intercom unit"></div>
      <div class="intercom-unit unit-back" role="img" aria-label="Second wireless intercom unit"></div>
      <h2 class="banner-title"><span class="line-1">Wireless</span><span class="line-2">Intercoms</span></h2>
    </div>

    <div class="products">
      <div class="product"><span class="thumb" role="img" aria-label="Portable intercom set"></span><h5>Portable Wireless Intercom System Set</h5><p class="price">Regular Price $149.00</p></div>
      <div class="product"><span class="tag"><i></i>staff pick</span><span class="thumb" role="img" aria-label="Intercom base stations"></span><h5>MURS 4-Mile Range Intercom Set: Base Stations by Northfield Alert</h5><p class="price">Regular Price $219.00</p></div>
      <div class="product"><span class="thumb" role="img" aria-label="Three-channel intercom set"></span><h5>Basic 3-Channel Intercom System Set</h5><p class="price">Regular Price $99.00</p></div>
      <div class="product"><span class="tag sale"><i></i>on sale</span><span class="thumb" role="img" aria-label="Wireless doorbell with intercom"></span><h5>Wireless Doorbell w/ Intercom</h5><p class="price">Regular Price $179.00</p></div>
    </div>
  </section>

  <section class="banner variant-light">
    <div class="intercom-unit unit-front" role="img" aria-label="Wireless intercom unit on a light background"></div>
    <div class="intercom-unit unit-back" role="img" aria-label="Second wireless intercom unit on a light background"></div>
    <h2 class="banner-title"><span class="line-1">Wireless</span><span class="line-2">Intercoms</span></h2>
  </section>

  <section class="banner variant-dark">
    <div class="intercom-unit unit-front" role="img" aria-label="Wireless intercom unit on a dark background"></div>
    <div class="intercom-unit unit-back" role="img" aria-label="Second wireless intercom unit on a dark background"></div>
    <h2 class="banner-title"><span class="line-1">Wireless</span><span class="line-2">Intercoms</span></h2>
  </section>

</body>
</html>
```